Commercial Construction Company

We need a business card design based on our current logo. We are a commercial general contractor based in Southern California that specializes in bank remodels. We would like to see designs that incorporate dark blue. The final design should portray an image of professionalism and quality.

If possible, I would like to add metallic foil to the design. Thank you

```html
<!DOCTYPE html>
<html lang="en">
<head>
<meta charset="utf-8">
<title>Harlow Commercial Builders — Business Card</title>
<link href="https://fonts.googleapis.com/css2?family=Lato:wght@400;700;900&display=swap" rel="stylesheet">
<style>
  :root {
    --stage: #2a2522;
    --card: #0b0b0d;
    --card-edge: #16161a;
    --blue: #1f63a8;
    --white: #f2f2f2;
    --ghost: #1c1c20;
    --divider: #2b3544;
  }
  * { box-sizing: border-box; margin: 0; padding: 0; }
  html, body { width: 1200px; height: 847px; overflow: hidden; }
  body {
    background: var(--stage);
    font-family: "Lato", sans-serif;
    position: relative;
  }
  .card {
    position: absolute;
    top: 275px;
    width: 520px;
    height: 298px;
    background: var(--card);
    border: 1px solid var(--card-edge);
    border-radius: 3px;
    box-shadow: 0 14px 30px rgba(0,0,0,.45);
    overflow: hidden;
  }
  .card--back { left: 50px; }
  .card--front { left: 630px; }

  /* back side */
  .back-mark {
    position: absolute;
    left: 70px; top: 80px;
    display: flex; align-items: center; gap: 18px;
  }
  .back-mark__dot {
    width: 70px; height: 70px; border-radius: 50%;
    background: var(--ghost);
  }
  .back-mark__name {
    font-weight: 900; font-size: 64px; letter-spacing: 2px;
    color: var(--ghost); line-height: 1;
  }
  .back-url {
    position: absolute; right: 34px; bottom: 28px;
    font-size: 15px; color: var(--white);
  }
  .back-url .accent { color: var(--blue); }

  /* front side */
  .brand {
    position: absolute; left: 36px; top: 134px;
    display: flex; align-items: center; gap: 10px;
  }
  .brand__dot {
    width: 28px; height: 28px; border-radius: 50%;
    background: var(--blue);
  }
  .brand__name {
    font-weight: 900; font-size: 30px; color: var(--white);
    letter-spacing: 1px; line-height: 1;
  }
  .divider {
    position: absolute; left: 242px; top: 70px;
    width: 1px; height: 160px; background: var(--divider);
  }
  .contact {
    position: absolute; left: 264px; top: 64px;
    color: var(--white);
  }
  .contact__name {
    font-weight: 700; font-size: 24px; color: var(--blue);
    letter-spacing: .5px; line-height: 1.1;
  }
  .contact__role { font-size: 15px; margin-bottom: 10px; }
  .contact__line { font-size: 14px; line-height: 1.35; }
  .contact__list { list-style: none; margin-top: 8px; }
  .contact__list li {
    display: flex; align-items: center; gap: 8px;
    font-size: 14px; line-height: 1.6;
  }
  .icon { width: 13px; height: 13px; flex: none; }
</style>
</head>
<body>

<section class="card card--back" aria-label="Card back">
  <div class="back-mark">
    <span class="back-mark__dot"></span>
    <span class="back-mark__name">HARLOW</span>
  </div>
  <p class="back-url">www.<span class="accent">harlowbuilders</span>.com</p>
</section>

<section class="card card--front" aria-label="Card front">
  <div class="brand">
    <span class="brand__dot"></span>
    <span class="brand__name">HARLOW</span>
  </div>
  <span class="divider"></span>
  <div class="contact">
    <h1 class="contact__name">DANIEL REYES</h1>
    <p class="contact__role">Founder &amp; CEO</p>
    <p class="contact__line">1234 First Line Address</p>
    <p class="contact__line">5678 Second Line Address</p>
    <ul class="contact__list">
      <li>
        <svg class="icon" viewBox="0 0 16 16" aria-hidden="true"><path fill="var(--blue)" d="M3.5 1h3l1.2 3.5-1.8 1.2a9 9 0 0 0 4.4 4.4l1.2-1.8L15 9.5v3a2 2 0 0 1-2 2A12.5 12.5 0 0 1 1.5 3a2 2 0 0 1 2-2z"/></svg>
        1234567890
      </li>
      <li>
        <svg class="icon" viewBox="0 0 16 16" aria-hidden="true"><rect x="1" y="3" width="14" height="10" fill="var(--blue)"/><path d="M1 3l7 6 7-6" fill="none" stroke="var(--card)" stroke-width="1.4"/></svg>
        info@harlowbuilders.com
      </li>
      <li>
        <svg class="icon" viewBox="0 0 16 16" aria-hidden="true"><g fill="none" stroke="var(--blue)" stroke-width="1.4"><circle cx="8" cy="8" r="6.5"/><ellipse cx="8" cy="8" rx="2.8" ry="6.5"/><path d="M1.5 8h13"/></g></svg>
        www.harlowbuilders.com
      </li>
    </ul>
  </div>
</section>

</body>
</html>
```